BrightHarbor Web Design Project

BrightHarbor IT solutions, a IT mananaged services company is looking to redesign current website (brightharborsolutions.example).

The website should convey professionalism within the managed it services community. The layout should invite users to explore other areas of the site. Should contain tools and other current information that clients or potential clients would find useful. Product pages, special offers and informational pages should be easily editable by non-programmers. Tidewardnet.example is a good site to review as an example of the design components we like.

Target Market(s)

Professional services companies with 10-100 users

Industry/Entity Type

It Company

Requirements
Must have
• • Clickable icons and graphics are good
• SEO - Wordpress could be a great platform for us to work from as we already have internal experience with it and it’s easy to update. If not Wordpress, we would need something that is easy to SEO optimize
• An “our team” section with pictures
• Sell the message to potential clients why they need managed services
• Home page needs to convey our core services at a glance
• Home page needs to load quickly
• Screenshots of our monitoring and security reports
• Easy for us to update/edit certain areas
o New products
o Testimonials
Nice to have
• • Something like TN’s savings calculator - http://www.tidewardnet.example/it-savings-calculator/
• Webform to enter service ticket requests
• Motion of home page banner
• Maybe pull in RSS feeds from current tech news sources
• Rotating content on all pages to keep it fresh
• “Harbor-up” feature for monthly promos
Should not have
• • Should not be overly "techie" in feel.
• Not overly wordy (like current site)

```html
<!DOCTYPE html>
<html lang="en">
<head>
<meta charset="utf-8">
<title>BrightHarbor IT Solutions</title>
<link rel="stylesheet" href="https://fonts.googleapis.com/css2?family=Ubuntu:wght@400;500&family=Arimo:wght@400;700&display=swap">
<style>
  :root{
    --lime:#8fd11e;
    --lime-dark:#6aa413;
    --green-text:#5c9a12;
    --nav-dark:#3d3e40;
    --nav-mid:#55575a;
    --panel:#ffffff;
    --ink:#222222;
    --muted:#8c8c8c;
    --line:#e2e2e2;
    --footer:#4a4a4a;
    --orange:#f07a12;
    --sky:#1aa6e0;
    --rust:#a33a12;
    --olive:#5f8f14;
  }
  *{box-sizing:border-box;margin:0;padding:0}
  html,body{width:1200px;height:1190px;overflow:hidden}
  body{position:relative;background:linear-gradient(#f4f4f4,#e8e8e8 40%,#efefef);font-family:"Arimo",Arial,sans-serif;color:var(--ink)}
  .top-strip{position:absolute;left:0;top:0;width:1200px;height:8px;background:var(--lime)}
  .header{position:absolute;left:0;top:8px;width:1200px;height:80px;background:linear-gradient(#ffffff,#f1f1f1);border-bottom:1px solid #e4e4e4}
  .brand{position:absolute;left:48px;top:6px;display:flex;align-items:center;gap:14px}
  .brand-dot{width:70px;height:70px;border-radius:50%;background:var(--lime-dark)}
  .brand-name{font-weight:700;font-size:30px;color:var(--green-text)}
  .remote-btn{position:absolute;left:820px;top:32px;width:128px;height:27px;border-radius:4px;background:linear-gradient(#f3f3f3,#d6d6d6);border:1px solid #c9c9c9;color:#8a8a8a;font-weight:700;font-size:13px;line-height:25px;text-align:center}
  .contact-lines{position:absolute;right:51px;top:26px;text-align:right;font-weight:700;font-size:15px;line-height:28px}
  .contact-lines .phone{color:#111}
  .contact-lines .tollfree{color:var(--lime-dark)}

  .main-nav{position:absolute;left:47px;top:100px;width:1100px;height:52px;border-radius:7px 7px 0 0;background:linear-gradient(var(--nav-mid),var(--nav-dark));display:flex;border-bottom:4px solid var(--lime)}
  .main-nav a{display:block;height:48px;line-height:48px;text-align:center;color:var(--lime);font-family:"Ubuntu",sans-serif;font-size:16px;text-decoration:none;border-right:1px solid #2e2f30;box-shadow:1px 0 0 #5e6063}
  .content-panel{position:absolute;left:47px;top:155px;width:1100px;height:944px;background:var(--panel);box-shadow:0 1px 4px rgba(0,0,0,.12)}

  .hero{position:absolute;left:58px;top:168px;width:1075px;height:309px;background:#9bd820;border:2px solid var(--lime);overflow:hidden}
  .hero-art{position:absolute;right:0;top:0;width:560px;height:305px;background:linear-gradient(90deg,rgba(155,216,32,0),#7fbf1a 35%,#5ea410 70%,#79b41a)}
  .hero-copy{position:absolute;left:31px;top:90px;font-family:"Ubuntu",sans-serif;font-size:27px;line-height:37.5px;color:#fff;text-shadow:0 1px 2px rgba(0,0,0,.35)}

  .intro{position:absolute;left:60px;top:494px;width:790px}
  .intro h1{font-size:16.5px;line-height:26px;color:var(--green-text);font-weight:700}
  .intro h1 .strong{color:#111}
  .intro p{margin-top:9px;font-size:13px;line-height:21px;color:var(--muted)}
  .intro p + p{margin-top:5px}

  .service{position:absolute;width:392px;height:174px;border:1px solid var(--line);background:#fff}
  .service h2{height:41px;line-height:41px;padding-left:10px;font-size:15.5px;font-weight:700;border-bottom:1px solid var(--line);background:linear-gradient(#fff,#f8f8f8)}
  .service .thumb{position:absolute;left:11px;top:55px;width:151px;height:100px;background:linear-gradient(135deg,#1b2433,#2f4d7a 55%,#0f1622)}
  .service p{position:absolute;left:172px;top:53px;width:208px;font-size:13.3px;line-height:18.2px;color:#222}
  .service p b{margin-left:6px}
  .svc-consult{left:59px;top:691px}  .svc-consult h2{color:var(--orange)}
  .svc-programs{left:463px;top:691px} .svc-programs h2{color:var(--sky)}
  .svc-security{left:59px;top:878px} .svc-security h2{color:var(--rust)}
  .svc-backup{left:463px;top:878px} .svc-backup h2{color:var(--olive)}

  .news-bar{position:absolute;left:58px;top:1061px;width:801px;height:31px;background:#f1f1f1}
  .news-tag{position:absolute;left:0;top:0}
  .news-tag span{position:absolute;left:10px;top:0;line-height:31px;color:#fff;font-weight:700;font-size:15px}
  .news-text{position:absolute;left:90px;top:0;line-height:31px;font-size:13.5px;color:#222;white-space:pre}
  .news-more{position:absolute;right:0;top:0}
  .news-more span{position:absolute;right:11px;top:0;line-height:31px;color:#fff;font-size:13px}

  .side-head{position:absolute;left:868px;width:265px;height:40px;line-height:40px;padding-left:10px;color:#fff;font-family:"Ubuntu",sans-serif;font-size:18px}
  .side-head.dark{background:linear-gradient(#6e6f71,#3a3b3d)}
  .side-head.green{background:linear-gradient(#8ad21e,#5fa010)}
  .side-photo{position:absolute;left:868px;width:265px}
  .team-photo{top:534px;height:111px;background:linear-gradient(#f3f5f8,#c9d3df)}
  .product-photo{top:697px;height:175px;background:linear-gradient(160deg,#e8ebee,#b9c4cf 50%,#8a96a3)}
  .testimonials{position:absolute;left:868px;top:925px;width:265px;height:167px;border:1px solid var(--line);border-top:none;padding:0 14px 0 11px}
  .testimonials p{font-size:13px;line-height:18.5px;color:#222;padding:8px 0 9px;border-bottom:1px solid #dcdcdc}
  .testimonials p:last-of-type{border-bottom:none}
  .testimonials .more{position:absolute;right:12px;bottom:3px;font-size:13px;color:var(--lime-dark)}

  .footer{position:absolute;left:0;top:1109px;width:1200px;height:81px;background:var(--footer)}
  .footer-links{position:absolute;left:47px;top:17px;font-size:13.5px;color:#b5b5b5}
  .footer-links span{margin:0 7px;color:#9a9a9a}
  .copyright{position:absolute;right:53px;top:17px;font-size:13.5px;color:var(--lime)}
</style>
</head>
<body>
  <div class="top-strip"></div>
  <header class="header">
    <div class="brand"><div class="brand-dot"></div><span class="brand-name">BrightHarbor</span></div>
    <div class="remote-btn">Remote Support</div>
    <div class="contact-lines">
      <div class="phone">Phone: (555) 014-2280</div>
      <div class="tollfree">Toll Free: (800) 555-0147</div>
    </div>
  </header>

  <nav class="main-nav">
    <a style="width:75px">Home</a>
    <a style="width:102px">Solutions</a>
    <a style="width:100px">About Us</a>
    <a style="width:94px">Contact</a>
    <a style="width:152px">Remote Support</a>
    <a style="width:132px">IT Consulting</a>
    <a style="width:121px">IT Programs</a>
    <a style="width:116px">IT Security</a>
    <a style="width:125px">Data Backup</a>
  </nav>

  <div class="content-panel"></div>

  <section class="hero">
    <div class="hero-art" role="img" aria-label="Young seedling growing from a mound of soil beside tall green grass"></div>
    <div class="hero-copy">Every Company Needs to Grow to Survive.<br>We Make sure your technology<br>Is ready for that growth when you are</div>
  </section>

  <section class="intro">
    <h1>Bright<span class="strong">Harbor</span> can help your business harness the power of new technology, making your business fast and efficient.</h1>
    <p>In the information age of today, one must stay abreast of current technology in order to thrive. New advancements are made daily in dispersing information and collaborative computing.</p>
    <p>High-speed networks aid in the exchange of electronic information between businesses, their customers, vendors, and peers. Businesses that are quick to act and effectively implement this technology will rise to the top.</p>
  </section>

  <article class="service svc-consult">
    <h2>IT CONSULTING SERVICES</h2>
    <div class="thumb" role="img" aria-label="Support technician with headset working at a computer"></div>
    <p>Insure that your existing system receives quality service. Bright-Harbor will troubleshoot problems, install new software or parts, and keep your system in optimal condition...<b>Read More...</b></p>
  </article>
  <article class="service svc-programs">
    <h2>IT SERVICE PROGRAMS</h2>
    <div class="thumb" role="img" aria-label="Support technician with headset working at a computer"></div>
    <p>Insure that your existing system receives quality service. Bright-Harbor will troubleshoot problems, install new software or parts, and keep your system in optimal condition...<b>Read More...</b></p>
  </article>
  <article class="service svc-security">
    <h2>SECURITY VULNERABILITY SCAN</h2>
    <div class="thumb" role="img" aria-label="Support technician with headset working at a computer"></div>
    <p>Insure that your existing system receives quality service. Bright-Harbor will troubleshoot problems, install new software or parts, and keep your system in optimal condition...<b>Read More...</b></p>
  </article>
  <article class="service svc-backup">
    <h2>DATA BACKUP AND RECOVERY</h2>
    <div class="thumb" role="img" aria-label="Support technician with headset working at a computer"></div>
    <p>Insure that your existing system receives quality service. Bright-Harbor will troubleshoot problems, install new software or parts, and keep your system in optimal condition...<b>Read More...</b></p>
  </article>

  <div class="news-bar">
    <div class="news-tag">
      <svg width="76" height="31"><polygon points="0,0 62,0 76,15.5 62,31 0,31" fill="#b9b9b9"/></svg>
      <span>NEWS</span>
    </div>
    <div class="news-text">Lorem ipsum dolor sit ipsum Lorem ipsum dolor sit ipsum  Lorem ipsum dolor sit ipsum</div>
    <div class="news-more">
      <svg width="76" height="31"><polygon points="14,0 76,0 76,31 14,31 0,15.5" fill="#b9b9b9"/></svg>
      <span>More...</span>
    </div>
  </div>

  <div class="side-head dark" style="top:490px">Our Team</div>
  <div class="side-photo team-photo" role="img" aria-label="Group portrait of the support team in business attire"></div>
  <div class="side-head green" style="top:657px">New Product</div>
  <div class="side-photo product-photo" role="img" aria-label="Staff member with a laptop in a warehouse"></div>
  <div class="side-head dark" style="top:885px">Testimonials</div>
  <div class="testimonials">
    <p>Lorem ipsum dolor sit ipsum Lorem ipsum dolor sit ipsum</p>
    <p>Lorem ipsum dolor sit ipsum Lorem ipsum dolor sit ipsum</p>
    <p>Lorem ipsum dolor sit ipsum Lorem ipsum dolor sit ipsum</p>
    <span class="more">More..</span>
  </div>

  <footer class="footer">
    <div class="footer-links">Home<span>|</span>Solutions<span>|</span>About Us<span>|</span>Contact<span>|</span>Carrer<span>|</span>Sitemap</div>
    <div class="copyright">Copyright @ 2012 BrightHarbor Company</div>
  </footer>
</body>
</html>
```